Building company requiring web site design

We need a web design for a new company based in Sydney called Marlow Building Co. We build and renovate new and existing homes for consumers. We would like to see design that use the colours red and grey. The final design should communicate innovative building but with old fashion quality, great customer service and attention to detail. I have already had a logo and stationary design completed and would like to use the these colour schemes
Updates

Target Market(s)

Home owners, investors

Industry/Entity Type

Building

Coding

Coded - Design and coding required

Number of Pages Required

5+ page

Requirements
Must have
• Home page, contact page, about us page, gallery page and testimonial page
Nice to have
• Contact form

```html
<!DOCTYPE html>
<html lang="en">
<head>
<meta charset="utf-8">
<title>Marlow Building Co.</title>
<link href="https://fonts.googleapis.com/css2?family=Raleway:ital,wght@0,400;0,500;0,600;0,700;0,800;1,400&display=swap" rel="stylesheet">
<style>
:root{
  --red:#d9443d;
  --red-dark:#c23a34;
  --ink:#222;
  --text:#555;
  --muted:#888;
  --line:#e3e3e3;
  --grey-bg:#f4f4f4;
  --dark:#3a3a3a;
  --footer:#efefef;
  --copy:#4a4a4a;
  --white:#fff;
}
*{box-sizing:border-box;margin:0;padding:0}
html,body{width:1200px;height:3965px;overflow:hidden}
body{font-family:"Raleway",sans-serif;color:var(--text);background:var(--white);font-size:15px;line-height:1.6}
.wrap{width:1084px;margin:0 auto;position:relative}
.btn{display:inline-block;background:var(--red);color:var(--white);font-weight:700;font-size:12px;letter-spacing:1px;text-transform:uppercase;border-radius:26px;padding:0 28px;height:48px;line-height:48px}
.sec-title{text-align:center;font-size:29px;font-weight:700;color:var(--ink);letter-spacing:.5px}
.sec-title::after{content:"";display:block;width:70px;height:2px;background:var(--red);margin:22px auto 0}
.sec-lead{text-align:center;font-size:15px;line-height:28px;max-width:800px;margin:0 auto}
.photo{display:block}

/* top bar */
.topbar{height:48px;border-bottom:1px solid var(--line);font-size:12px;color:var(--muted)}
.topbar .wrap{display:flex;align-items:center;height:48px}
.topbar .info{display:flex;gap:44px;margin-left:40px}
.topbar .info span{display:flex;align-items:center;gap:8px}
.topbar .social{margin-left:auto;display:flex;height:48px}
.topbar .social i{width:40px;border-left:1px solid var(--line);display:flex;align-items:center;justify-content:center}
.topbar .social i::before{content:"";width:9px;height:9px;border-radius:50%;background:#aaa}

/* nav */
.nav{height:89px}
.nav .wrap{display:flex;align-items:center;height:89px;margin-left:66px;width:1076px}
.brand{display:flex;align-items:center;gap:10px;font-weight:800;font-size:19px;color:var(--ink)}
.brand i{width:26px;height:26px;background:var(--red)}
.menu{margin-left:auto;display:flex;gap:6px;font-size:12px;font-weight:600;color:var(--ink);text-transform:uppercase}
.menu a{padding:8px 12px}
.menu a.active{background:var(--red);color:var(--white)}

/* hero */
.hero{height:524px;position:relative;background:linear-gradient(110deg,#6b5140 0%,#b06a32 25%,#c9d6e0 50%,#9fbad3 75%,#c2a06c 100%)}
.hero-box{position:absolute;left:66px;top:130px;width:418px;height:280px;background:rgba(30,30,30,.8);padding:26px 28px;color:var(--white)}
.hero-box h1{font-size:27px;line-height:35px;font-weight:700;text-transform:uppercase}
.hero-box p{margin-top:22px;font-size:14px;line-height:22px;color:#ddd}
.hero-box .btn{margin-top:24px;background:#2e2e2e;border:1px solid #444;height:44px;line-height:44px;font-size:11px}

/* estimate */
.estimate{height:145px;border-bottom:1px solid var(--line)}
.estimate .wrap{display:flex;align-items:center;height:145px}
.estimate .icon{width:68px;height:68px;border:1px solid var(--line);border-radius:50%;display:flex;align-items:center;justify-content:center;margin-left:8px}
.estimate .copy{margin-left:32px}
.estimate h3{font-size:19px;font-weight:700;color:var(--ink);text-transform:uppercase}
.estimate p{font-size:14px;color:var(--text)}
.estimate .btn{margin-left:auto;padding:0 26px;height:46px;line-height:46px}

/* services */
.services{background:var(--grey-bg);height:793px;padding-top:60px}
.services .sec-lead{margin-top:34px}
.cards{display:flex;margin-top:40px}
.card{width:361px;background:var(--white);height:397px}
.card .photo{height:238px}
.card h4{text-align:center;font-size:17px;font-weight:700;color:var(--ink);text-transform:uppercase;margin-top:26px;letter-spacing:.5px}
.card p{text-align:center;font-size:13px;line-height:24px;margin:28px 48px 0}
.services .more{text-align:center;margin-top:42px}

/* projects */
.projects{height:616px;padding-top:48px;background:var(--white)}
.projects .sec-lead{margin-top:30px}
.gallery{display:flex;margin-top:32px}
.gallery .photo{width:300px;height:243px}
.explore{background:var(--grey-bg);height:138px;display:flex;align-items:center;justify-content:center;gap:44px}
.explore h3{font-size:21px;font-weight:700;color:var(--ink);text-transform:uppercase;letter-spacing:.5px}

/* about */
.about{height:737px;padding-top:48px}
.about .sec-lead{margin-top:30px}
.about-body{display:flex;margin-top:46px}
.about-body .photo{width:444px;height:444px;border-radius:50%;margin-left:4px}
.features{margin-left:116px;padding-top:38px}
.feature{display:flex;margin-bottom:40px}
.feature .ficon{width:82px;height:82px;border:1px solid var(--line);border-radius:50%;flex:none;display:flex;align-items:center;justify-content:center}
.feature .fcopy{margin-left:24px;width:430px}
.feature h4{font-size:17px;font-weight:700;color:var(--ink);text-transform:uppercase}
.feature p{font-size:13px;line-height:24px;margin-top:10px}

/* testimonial */
.testimonial{height:465px;position:relative;background:linear-gradient(120deg,#555 0%,#6d6660 40%,#7a6a55 70%,#5b5b5b 100%);color:var(--white);text-align:center}
.testimonial .quote-icon{position:absolute;left:559px;top:42px;width:82px;height:82px;border:2px solid rgba(255,255,255,.8);border-radius:50%;display:flex;align-items:center;justify-content:center}
.testimonial .quote-icon::after{content:"";position:absolute;bottom:-32px;left:40px;width:1px;height:30px;background:rgba(255,255,255,.8)}
.testimonial blockquote{position:absolute;left:170px;right:170px;top:196px;font-size:19px;line-height:34px;font-style:italic;font-weight:400}
.testimonial .who{position:absolute;left:0;right:0;top:366px;font-size:11px;font-weight:700;text-transform:uppercase;letter-spacing:.5px;line-height:22px}
.testimonial .arrow{position:absolute;top:238px;width:54px;height:54px;border:2px solid rgba(255,255,255,.8);border-radius:50%;display:flex;align-items:center;justify-content:center}

/* contact strip */
.contact-strip{height:133px;background:var(--red);color:var(--white)}
.contact-strip .wrap{display:flex;align-items:center;height:133px}
.citem{display:flex;align-items:center;width:370px}
.citem .cicon{width:80px;height:80px;border-radius:50%;background:var(--white);display:flex;align-items:center;justify-content:center;flex:none}
.citem .ctext{margin-left:24px;font-size:15px;line-height:24px}
.citem .ctext b{font-weight:700}

/* footer */
.footer{height:362px;background:var(--footer);padding-top:44px}
.footer .wrap{display:flex}
.fcol{width:280px}
.fcol h5{font-size:14px;font-weight:700;color:var(--ink);padding-bottom:10px;border-bottom:1px solid #ddd;margin-bottom:16px;width:210px}
.fcol p{font-size:13px;line-height:23px;width:210px}
.fsocial{display:flex;gap:0;margin-top:18px}
.fsocial i{width:46px;height:46px;background:var(--red);border-right:1px solid var(--red-dark);display:flex;align-items:center;justify-content:center}
.fsocial i::before{content:"";width:10px;height:10px;border-radius:50%;background:var(--white)}
.flist li{list-style:none;font-size:13px;line-height:28px;display:flex;align-items:center;gap:12px}
.tags{display:flex;flex-wrap:wrap;gap:8px 6px;width:230px}
.tags span{border:1px solid #d6d6d6;font-size:9px;text-transform:uppercase;letter-spacing:1px;padding:6px 9px;color:var(--muted)}
.post{display:flex;gap:14px;margin-bottom:18px}
.post .photo{width:70px;height:70px;flex:none}
.post h6{font-size:13px;font-weight:500;color:var(--ink);line-height:20px}
.post small{font-size:11px;color:var(--muted)}
.copyright{height:53px;background:var(--copy);color:#ddd;font-size:12px;text-align:center;line-height:53px}
</style>
</head>
<body>

<header class="topbar">
  <div class="wrap">
    <div class="info">
      <span><svg width="12" height="12" viewBox="0 0 24 24"><path fill="#999" d="M6.6 10.8a15 15 0 006.6 6.6l2.2-2.2c.3-.3.7-.4 1-.2 1.1.4 2.3.6 3.6.6.6 0 1 .4 1 1V20c0 .6-.4 1-1 1A17 17 0 013 4c0-.6.4-1 1-1h3.5c.6 0 1 .4 1 1 0 1.3.2 2.5.6 3.6.1.3 0 .7-.2 1z"/></svg>+61 2 9000 4821</span>
      <span><svg width="12" height="12" viewBox="0 0 24 24"><path fill="none" stroke="#999" stroke-width="2" d="M3 5h18v14H3zM3 5l9 8 9-8"/></svg>info@marlowbuilding.com</span>
      <span><svg width="12" height="12" viewBox="0 0 24 24"><circle cx="12" cy="12" r="9" fill="none" stroke="#999" stroke-width="2"/><path d="M12 7v5l3 2" stroke="#999" stroke-width="2" fill="none"/></svg>Mon - Fri: 08:00 - 17:00</span>
    </div>
    <div class="social"><i></i><i></i><i></i><i></i><i></i></div>
  </div>
</header>

<nav class="nav">
  <div class="wrap">
    <div class="brand"><i></i>Marlow Building Co.</div>
    <div class="menu">
      <a class="active">Home</a><a>Features</a><a>Services</a><a>Projects</a><a>News</a><a>Shop</a><a>Career</a><a>Contact</a>
    </div>
  </div>
</nav>

<section class="hero" role="img" aria-label="Orange excavator bucket against a blue sky on a construction site">
  <div class="hero-box">
    <h1>Your most affordable contractors</h1>
    <p>We have the experience, personel and resources to make the project run smoothly. We can ensure a job is done on time.</p>
    <span class="btn">Buy this theme</span>
  </div>
</section>

<section class="estimate">
  <div class="wrap">
    <div class="icon"><svg width="32" height="32" viewBox="0 0 32 32" fill="none" stroke="#d9443d" stroke-width="2"><rect x="5" y="5" width="22" height="22" rx="3"/><circle cx="16" cy="17" r="5"/><path d="M9 10h6"/></svg></div>
    <div class="copy">
      <h3>Cost of renovation</h3>
      <p>Use our form to estimate the initial cost of renovation or installation</p>
    </div>
    <span class="btn">Request a quote</span>
  </div>
</section>

<section class="services">
  <div class="wrap">
    <h2 class="sec-title">OUR SERVICES</h2>
    <p class="sec-lead">With over 15 years experience and real focus on customer satisfaction, you can rely on us for your next renovation, driveway sett or home repair. We provide a professional service for private and commercial customers.</p>
    <div class="cards">
      <div class="card">
        <div class="photo" role="img" aria-label="Hands measuring a wooden floor with a tape measure" style="background:linear-gradient(135deg,#d9a56d,#b87a45)"></div>
        <h4>Interior renovation</h4>
        <p>We can help you bring new life to existing rooms and develop unused spaces.</p>
      </div>
      <div class="card">
        <div class="photo" role="img" aria-label="Red bricks being laid with a spirit level" style="background:linear-gradient(135deg,#e9d3b0,#c0603a)"></div>
        <h4>Design and build</h4>
        <p>From initial design and project specification to archieving a high end finish.</p>
      </div>
      <div class="card">
        <div class="photo" role="img" aria-label="Worker cutting floor tiles" style="background:linear-gradient(135deg,#d6c7a8,#8c7b62)"></div>
        <h4>Tiling and painting</h4>
        <p>We offer quality tiling and painting solutions for interior and exterior.</p>
      </div>
    </div>
    <div class="more"><span class="btn">View all services</span></div>
  </div>
</section>

<section class="projects">
  <h2 class="sec-title">RECENT PROJECTS</h2>
  <p class="sec-lead" style="max-width:760px">Here are a few of many projects we have completed for our customers. We provide a professional service which includes consultation, free estimate, design, supply of materials and installation.</p>
  <div class="gallery">
    <div class="photo" role="img" aria-label="Bright renovated living room" style="background:linear-gradient(135deg,#e8e4df,#b9967c)"></div>
    <div class="photo" role="img" aria-label="Garden path and timber furniture" style="background:linear-gradient(135deg,#5f7a3c,#9a7a5a)"></div>
    <div class="photo" role="img" aria-label="Plumber fixing a sink" style="background:linear-gradient(135deg,#dcdcdc,#6d7f95)"></div>
    <div class="photo" role="img" aria-label="Solar panels installed on a tiled roof" style="background:linear-gradient(135deg,#7fa8d6,#3b5f9a 60%,#c2663e)"></div>
  </div>
  <div class="explore">
    <h3>Explore our projects</h3>
    <span class="btn">View all projects</span>
  </div>
</section>

<section class="about">
  <div class="wrap">
    <h2 class="sec-title">ABOUT US</h2>
    <p class="sec-lead" style="max-width:860px">We provide a professional renovation and installation services with a real focus on customer satisfaction. Our installations are carried out by fully trained staff to the highest professional standards.</p>
    <div class="about-body">
      <div class="photo" role="img" aria-label="Builder carrying timber planks outdoors" style="background:radial-gradient(circle at 40% 40%,#b8a98a,#5d7a3f 70%)"></div>
      <div class="features">
        <div class="feature">
          <div class="ficon"><svg width="36" height="36" viewBox="0 0 36 36" fill="none" stroke="#d9443d" stroke-width="2"><path d="M6 24a12 12 0 0124 0z"/><path d="M3 24h30v4H3z"/><path d="M18 12V9"/></svg></div>
          <div class="fcopy"><h4>Over 15 years experience</h4><p>We combine quality workmanship, superior knowledge and low prices to provide you with service unmatched by our competitors.</p></div>
        </div>
        <div class="feature">
          <div class="ficon"><svg width="36" height="36" viewBox="0 0 36 36" fill="none" stroke="#d9443d" stroke-width="2"><rect x="6" y="5" width="22" height="9" rx="2"/><path d="M28 9h3v8H17v4"/><rect x="15" y="21" width="4" height="10"/></svg></div>
          <div class="fcopy"><h4>Best materials</h4><p>We have the experience, personel and resources to make the project run smoothly. We can ensure a job is done on time.</p></div>
        </div>
        <div class="feature">
          <div class="ficon"><svg width="36" height="36" viewBox="0 0 36 36" fill="none" stroke="#d9443d" stroke-width="2"><path d="M5 10h20v8H5z"/><path d="M25 12h6v4h-6"/><path d="M10 18l-2 12h6l2-12"/></svg></div>
          <div class="fcopy"><h4>Professional standards</h4><p>Work with us involve a carefully planned series of steps, centered around a schedule we stick to and daily communication.</p></div>
        </div>
      </div>
    </div>
  </div>
</section>

<section class="testimonial" role="img" aria-label="Builder working at a site, darkened behind the testimonial">
  <div class="quote-icon"><svg width="38" height="38" viewBox="0 0 38 38" fill="none" stroke="#fff" stroke-width="2"><path d="M4 6h20v13H12l-5 5v-5H4z"/><path d="M27 12h7v13h-3v5l-5-5H14v-3"/></svg></div>
  <div class="arrow" style="left:60px"><svg width="16" height="16" viewBox="0 0 16 16"><path d="M10 3L5 8l5 5" stroke="#fff" stroke-width="2" fill="none"/></svg></div>
  <div class="arrow" style="right:60px"><svg width="16" height="16" viewBox="0 0 16 16"><path d="M6 3l5 5-5 5" stroke="#fff" stroke-width="2" fill="none"/></svg></div>
  <blockquote>"We would like to thank Marlow Company for an outstanding effort on this recently completed project located in the Moscow. The project involved a very aggressive schedule and it was completed on time. We would certainly like to use their professional services again."</blockquote>
  <div class="who">Daniel Hart<br>CEO of Harbour Lane Company</div>
</section>

<section class="contact-strip">
  <div class="wrap">
    <div class="citem">
      <div class="cicon"><svg width="34" height="34" viewBox="0 0 24 24"><path fill="none" stroke="#d9443d" stroke-width="1.6" d="M6.6 10.8a15 15 0 006.6 6.6l2.2-2.2c.3-.3.7-.4 1-.2 1.1.4 2.3.6 3.6.6.6 0 1 .4 1 1V20c0 .6-.4 1-1 1A17 17 0 013 4c0-.6.4-1 1-1h3.5c.6 0 1 .4 1 1 0 1.3.2 2.5.6 3.6.1.3 0 .7-.2 1z"/></svg></div>
      <div class="ctext">Phone:<br>+61 2 9000 4821</div>
    </div>
    <div class="citem">
      <div class="cicon"><svg width="36" height="36" viewBox="0 0 36 36" fill="none" stroke="#d9443d" stroke-width="2"><path d="M4 8l9-3 10 3 9-3v23l-9 3-10-3-9 3z"/><path d="M13 5v23M23 8v23"/></svg></div>
      <div class="ctext">18 Kent Street<br>Millers Point NSW 2000</div>
    </div>
    <div class="citem">
      <div class="cicon"><svg width="36" height="36" viewBox="0 0 36 36" fill="none" stroke="#d9443d" stroke-width="2"><path d="M5 14l13-9 13 9v16H5z"/><path d="M5 14l13 9 13-9"/></svg></div>
      <div class="ctext">E-mail:<br><b>info@marlowbuilding.com</b></div>
    </div>
  </div>
</section>

<footer class="footer">
  <div class="wrap">
    <div class="fcol">
      <h5>About Us</h5>
      <p>Founded by Arthur Hale back in 2000, Marlow has established itself as one of the greatest and prestigious providers of construction focused interior renovation services and building.</p>
      <div class="fsocial"><i></i><i></i><i></i><i></i></div>
    </div>
    <div class="fcol">
      <h5>Our Services</h5>
      <ul class="flist">
        <li><svg width="12" height="12" viewBox="0 0 12 12"><path d="M1 6l3 3 7-7" stroke="#d9443d" stroke-width="2" fill="none"/></svg>Interior Renovation</li>
        <li><svg width="12" height="12" viewBox="0 0 12 12"><path d="M1 6l3 3 7-7" stroke="#d9443d" stroke-width="2" fill="none"/></svg>Design and Build</li>
        <li><svg width="12" height="12" viewBox="0 0 12 12"><path d="M1 6l3 3 7-7" stroke="#d9443d" stroke-width="2" fill="none"/></svg>Tiling and Painting</li>
        <li><svg width="12" height="12" viewBox="0 0 12 12"><path d="M1 6l3 3 7-7" stroke="#d9443d" stroke-width="2" fill="none"/></svg>Paver Walkways</li>
        <li><svg width="12" height="12" viewBox="0 0 12 12"><path d="M1 6l3 3 7-7" stroke="#d9443d" stroke-width="2" fill="none"/></svg>Household Repairs</li>
        <li><svg width="12" height="12" viewBox="0 0 12 12"><path d="M1 6l3 3 7-7" stroke="#d9443d" stroke-width="2" fill="none"/></svg>Solar Systems</li>
      </ul>
    </div>
    <div class="fcol">
      <h5>Categories</h5>
      <div class="tags"><span>Build</span><span>Design</span><span>Flooring</span><span>Painting</span><span>Pavers</span><span>Plumbing</span><span>Renovation</span><span>Repairs</span><span>Solar systems</span><span>Tiling</span></div>
    </div>
    <div class="fcol">
      <h5>Latest Posts</h5>
      <div class="post">
        <div class="photo" role="img" aria-label="Renovated lounge room" style="background:linear-gradient(135deg,#a7b58a,#8a6a4a)"></div>
        <div><h6>What a Difference a Few Months Make</h6><small>April 25, 2015</small></div>
      </div>
      <div class="post">
        <div class="photo" role="img" aria-label="Renovated kitchen" style="background:linear-gradient(135deg,#e2d8c8,#9c7a5a)"></div>
        <div><h6>Kitchen and Living Room Renovation</h6><small>April 17, 2015</small></div>
      </div>
    </div>
  </div>
</footer>
<div class="copyright">Copyright © 2016 Marlow Building Co. All Right Reserved.</div>

</body>
</html>
```